Business Card design for a company called Tallow Flame NI

I need a business card design for my oil fired boiler servicing company. I have a logo design already and Im just looking that incorporated into the business card design. card details; Tallow Flame NI
Oil Burner Servicing - Mid Ulster Area
Service Engineer - Owen Marsh
Mobile 07751364927
email - Tallow.Flame.NI@hearthmail.example
www.tallowflameni.example
I carry out Servicing, Commissioning, Fault Finding, Warranty Validation
Target Market(s)
home owners with oil fired central heating
Industry/Entity Type
Business
Contact Information for Business Card
Tallow Flame NI
Tell. 07751364927
Web: www.tallowflameni.example
email Tallow.Flame.NI@Hearthmail.Example
Servicing Fault Finding Commissioning Warranty Validation
Look and feel

```html
<!DOCTYPE html>
<html lang="en">
<head>
<meta charset="utf-8">
<title>Tallow Flame NI – Business Card</title>
<link href="https://fonts.googleapis.com/css2?family=Open+Sans:wght@400;600;700&family=Varela+Round&display=swap" rel="stylesheet">
<style>
  :root {
    --lime: #c2dc2a;
    --green: #46b648;
    --green-mid: #7cc53a;
    --text-green: #5cb83a;
    --ink: #222222;
    --white: #ffffff;
    --backdrop: #eceeea;
  }
  * { box-sizing: border-box; margin: 0; padding: 0; }
  html, body { width: 1200px; height: 900px; overflow: hidden; }
  body {
    background: var(--backdrop);
    font-family: "Open Sans", Arial, sans-serif;
    position: relative;
  }
  .card {
    position: absolute;
    background: var(--white);
    border-radius: 14px;
    overflow: hidden;
    box-shadow: 0 6px 22px rgba(0,0,0,0.18);
  }

  /* Front */
  .card-front { left: 78px; top: 35px; width: 587px; height: 363px; }
  .front-band {
    position: absolute; left: 0; top: 28px; width: 100%; height: 100px;
    background: linear-gradient(180deg, var(--lime) 0%, var(--green) 100%);
  }
  .emblem-circle {
    position: absolute; border-radius: 50%; background: var(--white);
  }
  .card-front .emblem-circle { left: 218px; top: 8px; width: 138px; height: 138px; }
  .brand-name {
    position: absolute; left: 0; width: 100%; text-align: center;
    font-family: "Varela Round", "Open Sans", sans-serif;
    font-weight: 400; letter-spacing: 0.5px;
  }
  .card-front .brand-name { top: 140px; font-size: 42px; color: var(--text-green); }
  .tagline {
    position: absolute; left: 0; width: 100%; text-align: center;
    font-size: 11px; font-weight: 600; letter-spacing: 1.6px; text-transform: uppercase;
  }
  .card-front .tagline { top: 192px; color: var(--text-green); }
  .person {
    position: absolute; right: 375px; top: 265px; text-align: right;
  }
  .person-name { font-size: 18px; font-weight: 600; color: var(--text-green); line-height: 1.3; }
  .person-role { font-size: 15px; color: var(--ink); line-height: 1.4; }
  .contacts { position: absolute; left: 270px; top: 252px; list-style: none; }
  .contacts li {
    display: flex; align-items: center; gap: 12px;
    font-size: 15px; color: var(--ink); height: 24.5px;
  }
  .contacts svg { width: 11px; height: 11px; fill: var(--text-green); flex: none; }

  /* Back */
  .card-back {
    left: 390px; top: 507px; width: 565px; height: 348px;
    background: linear-gradient(180deg, var(--green-mid) 0%, var(--green) 100%);
  }
  .back-top { position: absolute; left: 0; top: 0; width: 100%; height: 78px; background: var(--lime); }
  .back-stripe { position: absolute; left: 0; top: 78px; width: 100%; height: 100px; background: var(--white); }
  .card-back .emblem-circle {
    left: 195px; top: 28px; width: 156px; height: 156px;
    background: var(--green-mid);
  }
  .card-back .brand-name { top: 192px; font-size: 40px; color: var(--white); }
  .card-back .tagline { top: 242px; color: var(--white); }
  .services {
    position: absolute; left: 0; top: 292px; width: 100%; text-align: center;
    font-size: 15px; font-weight: 600; color: var(--white);
  }
</style>
</head>
<body>

<section class="card card-front" aria-label="Business card front">
  <div class="front-band"></div>
  <div class="emblem-circle"></div>
  <h1 class="brand-name">Tallow Flame NI</h1>
  <p class="tagline">Oil Burner Servicing - Mid Ulster Area</p>
  <div class="person">
    <p class="person-name">Owen Marsh</p>
    <p class="person-role">Service Engineer</p>
  </div>
  <ul class="contacts">
    <li>
      <svg viewBox="0 0 24 24" aria-hidden="true"><path d="M6.6 10.8a15.1 15.1 0 0 0 6.6 6.6l2.2-2.2c.3-.3.7-.4 1-.2 1.1.4 2.3.6 3.6.6.6 0 1 .4 1 1V20c0 .6-.4 1-1 1A17 17 0 0 1 3 4c0-.6.4-1 1-1h3.5c.6 0 1 .4 1 1 0 1.3.2 2.5.6 3.6.1.3 0 .7-.2 1z"/></svg>
      07751364927
    </li>
    <li>
      <svg viewBox="0 0 24 24" aria-hidden="true"><path d="M2 5h20v14H2z M2 5l10 8 10-8" /><path d="M2 5h20L12 13z" fill="#fff"/></svg>
      Tallow.Flame.NI@Hearthmail.Example
    </li>
    <li>
      <svg viewBox="0 0 24 24" aria-hidden="true"><circle cx="12" cy="12" r="11"/><path d="M7 8c2 0 3 1 3 3s-2 2-2 4M15 5c-1 2 1 3 2 4s2 3 0 5" stroke="#fff" stroke-width="2" fill="none"/></svg>
      www.tallowflameni.example
    </li>
  </ul>
</section>

<section class="card card-back" aria-label="Business card back">
  <div class="back-top"></div>
  <div class="back-stripe"></div>
  <div class="emblem-circle"></div>
  <h2 class="brand-name">Tallow Flame NI</h2>
  <p class="tagline">Oil Burner Servicing - Mid Ulster Area</p>
  <p class="services">Servicing | Fault Finding | Commissioning | Warranty Validation</p>
</section>

</body>
</html>
```